label design for oral care product

Kindly invite you to design bottle label (114 mm*40 mm) for our product, a kind of oral care product. The GEL is different from our previous cleanser product, as the pic we uploaded for demonstration. The color of frosted glass bottle is dark green, but the cap is white. You could download the pic of bottle among the uploaded files. The logo file and label content description are attached too. Please check them. Our product is made from many kinds of natural plant extracts, which includes herb and fruit. I wish the label would make our product look high-end and reliable. And it would be better if you could give some advice on paper material and special requirements for printing, related to your design. I value the texture of label too, because I think that stands for the quality of products. No color limitation for the use of our logo.
20-40 female, who value oral health.

```html
<!DOCTYPE html>
<html lang="en">
<head>
<meta charset="utf-8">
<title>Mint Lark Aligner Gel – Bottle Label</title>
<link rel="stylesheet" href="https://fonts.googleapis.com/css2?family=Montserrat:wght@500;600;700;800&display=swap">
<style>
  :root {
    --teal-deep: #3a8391;
    --teal-dark: #2f7482;
    --teal-light: #76b9c2;
    --stripe-grey: #c9ced1;
    --ink: #28474f;
    --white: #ffffff;
    --page: #e8ebec;
  }
  * { box-sizing: border-box; margin: 0; padding: 0; }
  html, body {
    width: 1200px; height: 900px; overflow: hidden;
    background: var(--page);
    font-family: "Montserrat", sans-serif;
  }
  .label {
    position: absolute; left: 48px; top: 256px;
    width: 1104px; height: 387px;
    border-radius: 18px; overflow: hidden;
    background: var(--teal-light);
  }
  .label__top-band {
    position: absolute; left: 0; top: 0; width: 100%; height: 150px;
    background: var(--teal-deep);
  }
  .label__stripe {
    position: absolute; left: 0; top: 150px; width: 100%; height: 7px;
    background: var(--stripe-grey);
  }
  .label__bottom-band {
    position: absolute; left: 0; bottom: 0; width: 100%; height: 30px;
    background: var(--teal-dark);
    color: var(--white); font-weight: 700; font-size: 16px;
    display: flex; align-items: center; justify-content: center;
  }
  .brand {
    position: absolute; left: 0; top: 30px; width: 100%;
    display: flex; align-items: center; justify-content: center; gap: 10px;
    color: var(--white); font-weight: 800; font-size: 42px; letter-spacing: -0.5px;
    line-height: 1;
  }
  .brand__dot {
    width: 14px; height: 14px; border-radius: 50%; background: var(--white);
  }
  .product-name {
    position: absolute; left: 369px; top: 115px; width: 366px; height: 72px;
    background: var(--teal-deep);
    border: 5px solid var(--stripe-grey); border-radius: 14px;
    color: var(--white); font-weight: 600; font-size: 43px; letter-spacing: 0.5px;
    display: flex; align-items: center; justify-content: center;
  }
  .claim {
    position: absolute; left: 0; top: 200px; width: 100%;
    text-align: center; color: var(--white);
  }
  .claim__kicker { font-weight: 700; font-size: 17px; line-height: 22px; }
  .claim__headline {
    font-weight: 600; font-size: 33px; letter-spacing: 1.5px; line-height: 40px;
  }
  .claim__rule {
    position: absolute; left: 432px; top: 263px; width: 240px; height: 2px;
    background: var(--white);
  }
  .tagline {
    position: absolute; left: 0; top: 277px; width: 100%;
    text-align: center; color: var(--ink);
    font-weight: 700; font-size: 16.5px; line-height: 21px;
  }
  .panel {
    position: absolute; top: 118px; width: 250px;
  }
  .panel--contains { left: 52px; }
  .panel--directions { left: 832px; }
  .panel__title {
    color: var(--white); font-weight: 700; font-size: 19px; letter-spacing: 0.3px;
    line-height: 22px;
  }
  .panel__body {
    margin-top: 30px;
    color: var(--ink); font-weight: 500; font-size: 15px; line-height: 21px;
    hyphens: auto;
  }
  .origin {
    position: absolute; left: 52px; top: 330px;
    color: var(--ink); font-weight: 700; font-size: 15px; letter-spacing: 1.2px;
  }
  .usage-icons {
    position: absolute; left: 826px; top: 294px;
    display: flex; gap: 22px;
  }
  .usage-icons svg { width: 42px; height: 42px; display: block; }
</style>
</head>
<body>
  <main class="label" lang="en">
    <div class="label__top-band"></div>
    <div class="label__stripe"></div>

    <div class="brand"><span class="brand__name">mint lark</span><span class="brand__dot"></span></div>

    <h1 class="product-name">ALIGNER GEL</h1>

    <div class="claim">
      <p class="claim__kicker">IMMUNE SUPPORT FOR</p>
      <p class="claim__headline">ORAL HEALTH</p>
    </div>
    <div class="claim__rule"></div>

    <p class="tagline">The Solution To Maintain<br>Dental Hygiene &amp;<br>Strengthen Gums</p>

    <section class="panel panel--contains">
      <h2 class="panel__title">CONTAINS:</h2>
      <p class="panel__body">A proprietary blend of natural plant extract including Angelica, Radix Rehmanniae, Coptis, Honeysuckle, Echinacea, Sage, Chamomile, Acerola cherry.</p>
    </section>
    <p class="origin">MADE IN TAIWAN</p>

    <section class="panel panel--directions">
      <h2 class="panel__title">DIRECTIONS:</h2>
      <p class="panel__body">Drop on the teeth directly after brushing. Or, put into clear aligners before wearing again. No need to rinse your mouth with water.</p>
    </section>

    <div class="usage-icons">
      <svg viewBox="0 0 42 42" aria-label="Dropper">
        <circle cx="21" cy="21" r="19" fill="var(--teal-deep)" stroke="var(--stripe-grey)" stroke-width="2"/>
        <path d="M26 11 l5 5 M24 13 l5 5 M26 16 l-11 11 l-3 1 l1 -3 l11 -11" fill="none" stroke="#fff" stroke-width="2.2" stroke-linecap="round" stroke-linejoin="round"/>
      </svg>
      <svg viewBox="0 0 42 42" aria-label="Tooth">
        <circle cx="21" cy="21" r="19" fill="var(--teal-deep)" stroke="var(--stripe-grey)" stroke-width="2"/>
        <path d="M15 11 c-4 0 -5 4 -4 8 c1 3 2 5 2 8 c0 3 1 5 3 5 c2 0 2 -6 5 -6 c3 0 3 6 5 6 c2 0 3 -2 3 -5 c0 -3 1 -5 2 -8 c1 -4 0 -8 -4 -8 c-2 0 -4 1 -6 1 c-2 0 -4 -1 -6 -1z" fill="none" stroke="#fff" stroke-width="2" stroke-linejoin="round"/>
      </svg>
      <svg viewBox="0 0 42 42" aria-label="Clear aligner">
        <circle cx="21" cy="21" r="19" fill="var(--teal-deep)" stroke="var(--stripe-grey)" stroke-width="2"/>
        <path d="M12 13 c0 10 4 17 9 17 c5 0 9 -7 9 -17 M16 13 c0 7 2 12 5 12 c3 0 5 -5 5 -12" fill="none" stroke="#fff" stroke-width="2.2" stroke-linecap="round"/>
      </svg>
    </div>

    <div class="label__bottom-band">30 ml / 1 fl oz</div>
  </main>
</body>
</html>
```